Flyer-Design für mobilen Mittagstisch
Zielgruppe
Wir liefern für eine Krankenhausküche Essen an Pflegebedürftige Menschen aus, und wir möchten einen übersichtlichen Flyer der die Leistungen, Preise, Lieferzeiten, eine BeispielspeisekarteKontaktdaten etc. beinhaltet.
Zielgruppe sind ältere Menschen bzw deren Betreuer oder Kinder.
Aufgabenstellung
Große Schrift , seriös, regional, Papierformat frei wählbar

```html
<!DOCTYPE html>
<html lang="de">
<head>
<meta charset="utf-8">
<title>Mittagstisch Waldhöhe – Flyer</title>
<link href="https://fonts.googleapis.com/css2?family=Noto+Serif:wght@400;700&family=PT+Sans:wght@400;700&display=swap" rel="stylesheet">
<style>
:root{
  --red:#cc1518;
  --red-line:#d8282b;
  --grey:#bdbdbd;
  --stone-1:#e4e3e1;
  --stone-2:#c9c8c5;
  --ink:#1d1d1d;
  --white:#ffffff;
  --backdrop:#ececec;
}
*{box-sizing:border-box;margin:0;padding:0}
html,body{width:866px;height:1200px;overflow:hidden}
body{background:var(--backdrop);font-family:"PT Sans",sans-serif;color:var(--ink);position:relative}
.spread{position:absolute;left:20px;width:826px;height:570px;overflow:hidden;box-shadow:0 6px 18px rgba(0,0,0,.25)}
.spread--inside{top:20px}
.spread--outside{top:610px;background:var(--white)}
.abs{position:absolute}

/* inside spread */
.stone{inset:0;background:linear-gradient(135deg,var(--stone-1),var(--stone-2) 60%,#d6d5d2)}
.veg{background:linear-gradient(180deg,#4f8a34,#c63a2a 55%,#9b9790)}
.veg--left{left:0;top:60px;width:40px;height:300px;border-radius:0 30px 30px 0}
.veg--right{right:0;top:40px;width:36px;height:460px;background:linear-gradient(180deg,#f1a91c,#4d8b2f 45%,#e9b020 80%,#8e8a83);border-radius:30px 0 0 30px}
.page-fold{left:412px;top:0;width:2px;height:570px;background:rgba(0,0,0,.12)}
.panel{background:rgba(247,247,246,.93);border:2px solid var(--red-line)}
.panel--how{left:48px;top:46px;width:318px;height:480px}
.panel--menu{left:452px;top:62px;width:330px;height:400px}
.tab{position:absolute;top:-14px;left:50%;transform:translateX(-50%);background:var(--red);color:var(--white);font-family:"Noto Serif",serif;font-size:11px;letter-spacing:.5px;padding:6px 18px;white-space:nowrap;text-transform:uppercase}
.panel-title{font-family:"Noto Serif",serif;font-weight:700;font-size:12.5px;text-align:center;line-height:1.3;margin-top:26px}
.how-text{padding:12px 22px 0;font-size:11px;line-height:1.35}
.how-text p{margin-bottom:11px}
.menu-table{margin:12px 14px 0;width:calc(100% - 28px);border-collapse:collapse;font-size:8.5px;line-height:1.25;text-align:center}
.menu-table th{font-family:"Noto Serif",serif;font-size:11.5px;padding-bottom:6px}
.menu-table td{padding:10px 4px;border-top:1px solid #555;vertical-align:middle}
.menu-table tr:nth-child(2) td{border-top:none}
.day{font-family:"Noto Serif",serif;font-weight:700;font-size:10px;writing-mode:vertical-rl;transform:rotate(180deg);letter-spacing:.5px;width:18px}
.badge{position:absolute;border-radius:50%;display:flex;align-items:center;justify-content:center;text-align:center;font-weight:700;line-height:1.25;border:4px solid var(--white)}
.badge--grey{background:var(--grey);color:var(--white)}
.badge--red{background:var(--red);color:var(--white)}
.badge--price-in{left:300px;top:430px;width:118px;height:118px;font-size:12.5px}
.badge--choose{left:660px;top:395px;width:132px;height:132px;font-size:13px}

/* outside spread */
.photo-guest{left:0;top:0;width:212px;height:146px;background:linear-gradient(135deg,#e7ebee,#d9c8b9 55%,#8bb068)}
.order-box{left:128px;top:86px;width:272px;height:110px;border:1.5px solid var(--red-line);background:var(--white);padding:14px 20px;color:var(--red);font-size:11.5px;line-height:1.7}
.order-box strong{font-size:12px}
.area{left:44px;top:212px;width:340px;font-size:11.2px;line-height:1.35}
.area strong{display:block}
.area p{margin-bottom:10px}
.photo-food{left:413px;top:0;width:413px;height:372px;background:linear-gradient(135deg,#e8eef3 0%,#f0a878 45%,#e8843f 65%,#7aa84a 80%,#f3de6a 100%)}
.brand-box{left:492px;top:0;width:270px;height:142px;background:var(--white);display:flex;flex-direction:column;align-items:center;justify-content:center;gap:8px}
.brand-dot{width:22px;height:22px;border-radius:50%;background:var(--red)}
.brand-name{font-family:"Noto Serif",serif;font-weight:700;color:var(--red);font-size:17px;letter-spacing:.5px;text-transform:uppercase}
.red-band{left:0;top:376px;width:826px;height:194px;background:var(--red)}
.badge--price-out{left:446px;top:248px;width:100px;height:100px;font-size:13.5px}
.badge--extra{left:252px;top:342px;width:150px;height:150px;font-size:11px;padding:12px}
.plate-circle{position:absolute;left:496px;top:320px;width:132px;height:132px;border-radius:50%;background:var(--white);display:flex;align-items:center;justify-content:center}
.imprint{left:40px;top:445px;color:var(--white);font-size:11px;line-height:1.45}
.imprint h2{font-size:11.5px;font-weight:700;letter-spacing:.4px;margin-bottom:12px}
.cta{left:460px;top:490px;width:340px;color:var(--white);font-size:16px;text-align:center;line-height:1.6}
.cta strong{font-weight:700;letter-spacing:.5px}
</style>
</head>
<body>

<section class="spread spread--inside" aria-label="Innenseiten">
  <div class="abs stone" role="img" aria-label="Hintergrund: heller Steintisch"></div>
  <div class="abs veg veg--left" role="img" aria-label="Basilikum und Tomaten am Rand"></div>
  <div class="abs veg veg--right" role="img" aria-label="Gelbe Tomaten, Kräuter und Pfefferkörner am Rand"></div>
  <div class="abs page-fold"></div>

  <article class="abs panel panel--how">
    <span class="tab">So funktioniert es</span>
    <h2 class="panel-title">Wir liefern Ihnen Ihr Mittagessen –<br>ganz einfach:</h2>
    <div class="how-text">
      <p>Wählen Sie aus drei leckeren Gerichten, inkl. Vor- und Nachspeise. Die Lieferung erfolgt in der darauffolgenden Woche frei Haus.</p>
      <p>Unser Menüplan hat jeden Tag ein Gericht als Vollkost, Schonkost oder vegetarischer Speise.</p>
      <p>Wählen Sie, ob Sie Ihr Mittagessen nur an bestimmten Tagen bekommen möchten, oder die ganze Woche.</p>
      <p>Wir liefern Ihr Essen in einer hochwertigen Menü-Wärmebox, auf Porzellantellern, diese holen wir auch wieder ab. Sie brauchen nur genießen – spülen erledigen wir.</p>
      <p>Berechnung erfolgt monatlich in einer detaillierten Sammelrechnung die dann überwiesen, oder per SEPA-Basislastschriftverfahren beglichen werden kann.</p>
    </div>
  </article>

  <article class="abs panel panel--menu">
    <span class="tab">Unser Speisenangebot</span>
    <h2 class="panel-title">Beispiel für einen wöchentlichen Menüplan</h2>
    <table class="menu-table">
      <tr><th></th><th>Menü 1</th><th>Menü 2</th><th>Menü 3</th></tr>
      <tr><td class="day">MONTAG</td><td>Überbackene Hähnchenbrust, Bratensoße, Bandnudeln und Salat</td><td>Gemüse-Frikadelle, Currysauce, Kartoffel, Salat</td><td>Gemüse-Frikadelle, Currysauce, Kartoffel, Salat</td></tr>
      <tr><td class="day">DIENSTAG</td><td>Überbackene Hähnchenbrust, Bratensoße, Bandnudeln und Salat</td><td>Gemüse-Frikadelle, Currysauce, Kartoffel, Salat</td><td>Gemüse-Frikadelle, Currysauce, Kartoffel, Salat</td></tr>
      <tr><td class="day">MITTWOCH</td><td>Überbackene Hähnchenbrust, Bratensoße, Bandnudeln und Salat</td><td>Gemüse-Frikadelle, Currysauce, Kartoffel, Salat</td><td>Gemüse-Frikadelle, Currysauce, Kartoffel, Salat</td></tr>
    </table>
  </article>

  <div class="badge badge--grey badge--price-in">nur € 8,90<br>pro Gericht inkl.<br>Vor- und Nach-<br>speise</div>
  <div class="badge badge--red badge--choose">Wählen Sie täglich<br>aus drei Gerichten<br>inkl. Vor- und<br>Nachspeise</div>
</section>

<section class="spread spread--outside" aria-label="Außenseiten">
  <div class="abs photo-guest" role="img" aria-label="Foto: ältere Dame mit einem Teller Salat"></div>

  <div class="abs order-box">
    <strong>Wir nehmen gerne Ihre Bestellung an:</strong><br>
    per E-Mail: bestellung@kalwer-kueche.de<br>
    per Telefon: 0 61 23 / 47 09<br>
    per Fax: 0 61 23 / 47 10
  </div>

  <div class="abs area">
    <p><strong>Unsere Liefergebiete sind die Verbandsgemeinden:</strong>Hermeskeil, Thalfang, Nonnweiler</p>
    <p><strong>Aktuell angefahrene Ortschaften sind:</strong>Hermeskeil (inkl. der Ortsteile Abtei, Höfchen, Lascheider Hof) Beuren, Bescheid, Rascheid, Malborn, Thiergarten, Damflos, Züsch, Neuhütten, Muhl, Nonnweiler, Primstal, Braunshausen, Kastel, Sötern, Kostenbach, Drohnecken, Hilscheid, Thalfang</p>
  </div>

  <div class="abs photo-food" role="img" aria-label="Foto: gegrilltes Lachsfilet mit Gemüse und Zitrone"></div>
  <div class="abs brand-box">
    <span class="brand-dot"></span>
    <span class="brand-name">Mittagstisch Waldhöhe</span>
  </div>

  <div class="abs red-band"></div>

  <div class="badge badge--grey badge--price-out">nur € 8,90<br>pro Gericht</div>
  <div class="badge badge--grey badge--extra">Auf Anfrage liefern wir auch Getränke bzw. Lebensmittel, Zeitungen, Haushaltsbedarf zum täglichen Bedarf</div>

  <div class="plate-circle">
    <svg width="90" height="56" viewBox="0 0 90 56" aria-hidden="true">
      <g fill="none" stroke="#222" stroke-width="3">
        <circle cx="45" cy="28" r="24"/>
        <circle cx="45" cy="28" r="17"/>
      </g>
      <g fill="#222">
        <rect x="8" y="18" width="4" height="36" rx="2"/>
        <ellipse cx="10" cy="12" rx="5" ry="10"/>
        <rect x="78" y="4" width="4" height="50" rx="2"/>
        <path d="M78 4 Q88 14 82 30 L78 30 Z"/>
      </g>
    </svg>
  </div>

  <div class="abs imprint">
    <h2>Impressum und Kontakt</h2>
    Jens Kalwer Frischküche GmbH &amp; Co KG<br>
    Lindenstieg 12<br>
    54400 Tannrode<br>
    info@kalwer-kueche.de
  </div>

  <div class="abs cta">
    Wählen Sie täglich aus drei Gerichten!<br>
    Jetzt testen: <strong>0 61 23 / 47 09</strong>
  </div>
</section>

</body>
</html>
```